Professional Website for Corvell Laundry Company

Corvell Laundry Company is a family-owned laundry service provider that has been serving Midtown Atlanta for over 45 years. We provide express clothing and linen washing services to residential and commercial clients in Atlanta and surrounding areas.

The final website and logo design should convey professionalism and give the customer a sense of security in having their personal items laundered with us.

Target Market(s)

Commercial Businesses and high net worth personal customers

Industry/Entity Type

Professional Laundry Services

Coding

Coded - Design and coding required

Number of Pages Required

5+ page

Font styles to use
Sans Serif

Colors
0054AA
0677BA
7BADD7
CADEEF
E8F1F8

Requirements
Must have
• I would like to have the following elements on my website: 1. Blog page 2. Contact Us Form 3. Sign up for service (sample attached) 4. Sections outlined in the content copy page 5. Links to social media accounts.
Nice to have
• A great example is https://www.quorvadip.example/laundry-pick-up-and-delivery/?utm_term=pick%20up%20and%20delivery%20laundry%20service&utm_campaign=*QV%20United%20States%20%7C%20Search%20(Broad%20KWs)&utm_source=bing&utm_medium=ppc&hsa_acc=1203948576&hsa_cam=50219384761&hsa_grp=9081726354637281&hsa_ad=&hsa_src=o&hsa_tgt=kwd-27391046582917:loc-190&hsa_kw=pick%20up%20and%20delivery%20laundry%20service&hsa_mt=e&hsa_net=bing&hsa_ver=3&msclkid=3a9f0c1b2d4e5f60718293a4b5c6d7e8

```html
<!DOCTYPE html>
<html lang="en">
<head>
<meta charset="utf-8">
<title>Corvell Laundry Company</title>
<link rel="stylesheet" href="https://fonts.googleapis.com/css2?family=Oswald:wght@300;400;500&family=Nunito+Sans:wght@400;600;700;800&display=swap">
<style>
:root{
  --cyan:#22b6e2;
  --cyan-dark:#0f9fcf;
  --navy:#0f1d35;
  --footer:#1b1e33;
  --red:#ec2a37;
  --yellow:#f7dd12;
  --ink:#333a45;
  --muted:#5a6270;
  --white:#ffffff;
  --line:#d9dde3;
}
*{box-sizing:border-box;margin:0;padding:0}
html,body{width:1200px;height:3653px;overflow:hidden}
body{font-family:"Nunito Sans",Arial,sans-serif;color:var(--ink);background:var(--white);position:relative}
section,header,footer{position:relative;width:1200px;overflow:hidden}
.abs{position:absolute}
.heading{font-family:"Oswald",Arial,sans-serif;text-transform:uppercase;line-height:1.1}
.btn{position:absolute;background:var(--red);color:var(--white);font-weight:800;font-size:13px;letter-spacing:1px;text-transform:uppercase;border-radius:22px;display:flex;align-items:center;justify-content:center;gap:6px}
.btn svg{width:7px;height:10px}
.photo{position:absolute}
/* top bar */
.topbar{height:37px}
.topbar-band{position:absolute;left:645px;top:0;width:555px;height:37px;background:var(--cyan);clip-path:polygon(0 0,100% 0,100% 100%,38px 100%)}
.topbar-info{position:absolute;right:173px;top:0;height:37px;display:flex;align-items:center;gap:22px;color:var(--white);font-size:13px}
.topbar-info span{display:flex;align-items:center;gap:6px}
.header{height:75px}
.brand{position:absolute;left:173px;top:0;display:flex;align-items:center;gap:8px}
.header .brand{top:-8px}
.brand-dot{width:20px;height:20px;border-radius:50%;border:2px solid var(--cyan)}
.brand-name{font-weight:700;font-size:14px;line-height:16px;color:var(--navy);text-align:center}
.nav{position:absolute;left:467px;top:22px;display:flex;gap:20px;font-size:13px;color:var(--ink)}
.nav .active{color:var(--cyan)}
/* hero */
.hero{height:438px;background:var(--cyan)}
.hero-photo{left:710px;top:0;width:490px;height:438px;background:linear-gradient(120deg,#3fc2e6 0%,#cfdde3 45%,#e8e4df 100%)}
.hero-kicker{left:173px;top:78px;color:var(--white);font-family:"Oswald",sans-serif;font-weight:300;font-size:29px;padding-left:12px;border-left:3px solid var(--navy);line-height:34px}
.hero-title{left:171px;top:118px;color:var(--white);font-weight:500;font-size:58px;line-height:66px}
.badge{left:564px;top:254px;width:156px;height:156px;border-radius:50%;background:var(--yellow);color:var(--navy);text-align:center;display:flex;flex-direction:column;justify-content:center;font-family:"Oswald",sans-serif}
.badge-ring{position:absolute;inset:8px;border:2px dashed var(--navy);border-radius:50%}
/* about */
.about{height:580px}
.about-photo{left:176px;top:67px;width:363px;height:421px;background:linear-gradient(160deg,#e9e6e2,#c9c2bb);border-radius:18px}
.dots{left:547px;top:140px;height:335px;border-left:3px dotted #b8bcc2}
.kicker{font-family:"Oswald",sans-serif;font-size:19px;letter-spacing:2px;color:var(--navy);text-transform:uppercase;font-weight:400}
.title{font-family:"Oswald",sans-serif;font-weight:500;color:var(--cyan);text-transform:uppercase;font-size:42px;line-height:46px}
.copy{font-size:14px;line-height:23px;color:var(--muted)}
/* services */
.services{height:474px;background:var(--navy);color:var(--white)}
.services .copy{color:#dfe4ec}
.svc-grid{left:597px;top:88px;width:430px;display:grid;grid-template-columns:repeat(3,1fr)}
.svc{height:150px;display:flex;flex-direction:column;align-items:center;justify-content:center;text-align:center;font-weight:700;font-size:14px;line-height:22px;gap:10px}
.svc:nth-child(3n+1),.svc:nth-child(3n+2){border-right:1px solid #3a4a66}
.svc:nth-child(-n+3){border-bottom:1px solid #3a4a66}
.svc-icon{width:44px;height:44px;border-radius:6px}
/* why */
.why{height:459px}
.why-photo{left:99px;top:55px;width:462px;height:277px;background:radial-gradient(ellipse at 45% 55%,#cbe0ee 0%,#e9eef2 55%,#ffffff 80%)}
/* blog */
.blog{height:543px;background:var(--navy)}
.card{position:absolute;top:135px;width:269px;height:349px;background:var(--white);border-radius:6px;overflow:hidden}
.card-photo{height:176px;background:linear-gradient(135deg,#9fb7c8,#e4e2dc)}
.date{position:absolute;left:12px;top:12px;width:42px;text-align:center;font-family:"Oswald",sans-serif}
.date-m{background:var(--navy);color:var(--white);font-size:10px;letter-spacing:1px;padding:1px 0}
.date-d{background:var(--cyan);color:var(--white);font-size:24px;line-height:30px}
.card-body{padding:16px 9px}
.card-title{font-weight:800;font-size:14px;color:var(--navy);margin-bottom:6px}
.card-text{font-size:14px;line-height:21px;color:#40454f}
.card-link{margin-top:18px;display:inline-flex;gap:5px;align-items:center;color:var(--cyan);font-weight:800;font-size:14px;letter-spacing:1px;border-bottom:1px solid var(--cyan);padding-bottom:2px}
.arrow{position:absolute;width:40px;height:40px;border-radius:50%;display:flex;align-items:center;justify-content:center}
/* contact */
.contact{height:492px}
.contact-card{left:173px;top:39px;width:854px;height:405px;background:var(--white);box-shadow:0 4px 20px rgba(0,0,0,.08)}
.contact-photo{left:0;top:0;width:407px;height:405px;background:linear-gradient(140deg,#d9d2c9,#a9b6c2)}
.field{position:absolute;left:437px;width:380px;border-bottom:1px solid #7a808a;font-size:13px;color:#4b515b;padding-bottom:14px}
/* newsletter */
.newsletter{height:170px;background:linear-gradient(90deg,#1bb0de,#3fc0e6,#1bb0de)}
.nl-title{right:663px;top:62px;color:var(--white);font-family:"Oswald",sans-serif;font-weight:300;font-size:37px;line-height:46px;white-space:nowrap;letter-spacing:-0.5px}
.nl-title b{font-weight:500}
.nl-input{left:553px;top:67px;width:404px;height:37px;background:var(--white);display:flex;align-items:center;justify-content:space-between;padding:0 12px 0 9px;font-size:14px;color:#444}
/* footer */
.footer{height:385px;background:var(--footer);color:#b9bfcc}
.f-col{position:absolute;top:67px;font-size:13px}
.f-col h4{color:var(--cyan);font-family:"Oswald",sans-serif;font-weight:400;font-size:13px;margin-bottom:15px}
.f-col li{list-style:none;line-height:32.6px}
.f-divider{position:absolute;top:58px;height:218px;border-left:1px solid #3b3f57}
.f-mark{position:absolute;width:3px;height:22px;background:var(--cyan);top:170px}
.social{position:absolute;top:156px;left:173px;display:flex;gap:6px}
.social span{width:32px;height:32px;background:var(--cyan);display:block}
.contact-row{display:flex;gap:8px;line-height:23px;margin-bottom:10px}
.contact-row svg{flex:none;margin-top:6px}
.bottom-line{position:absolute;left:173px;top:334px;width:854px;border-top:1px solid #3b3f57}
.copyright{position:absolute;left:223px;top:350px;font-size:12px;color:var(--cyan)}
.to-top{position:absolute;left:970px;top:334px;width:57px;height:51px;background:var(--cyan);color:var(--white);font-size:8px;font-weight:800;display:flex;flex-direction:column;align-items:center;justify-content:flex-end;padding-bottom:3px;gap:6px}
</style>
</head>
<body>

<header class="topbar">
  <div class="topbar-band"></div>
  <div class="topbar-info">
    <span><svg width="12" height="12" viewBox="0 0 24 24" fill="#fff"><path d="M6.6 10.8a15 15 0 0 0 6.6 6.6l2.2-2.2c.3-.3.7-.4 1-.2 1.1.4 2.3.6 3.6.6.6 0 1 .4 1 1V20c0 .6-.4 1-1 1A17 17 0 0 1 3 4c0-.6.4-1 1-1h3.5c.6 0 1 .4 1 1 0 1.3.2 2.5.6 3.6.1.3 0 .7-.2 1z"/></svg>01 234 567 890</span>
    <span><svg width="13" height="10" viewBox="0 0 24 18" fill="#fff"><path d="M0 0h24v18H0z M2 2l10 7 10-7" stroke="#22b6e2" stroke-width="1.5"/></svg>info@corvelllaundrycompany</span>
  </div>
</header>

<header class="header">
  <div class="brand" style="top:6px">
    <span class="brand-dot"></span>
    <span class="brand-name">Corvell<br>Laundry<br>Company</span>
  </div>
  <nav class="nav">
    <span class="active">Home</span><span>About Us</span><span>Why Choose Us</span><span>Services</span><span>Blog</span><span>Contact Us</span>
  </nav>
  <div class="btn" style="left:910px;top:14px;width:117px;height:38px">Sign Up <svg viewBox="0 0 7 10"><path d="M1 1l4 4-4 4" stroke="#fff" fill="none" stroke-width="1.5"/></svg></div>
</header>

<section class="hero">
  <div class="photo hero-photo" role="img" aria-label="Smiling woman holding a stack of freshly folded towels in a laundry room"></div>
  <div class="abs hero-kicker">CORVELL LAUNDRY COMPANY</div>
  <h1 class="abs heading hero-title">Is a family-owned<br>laundry service</h1>
  <div class="btn" style="left:173px;top:274px;width:217px;height:44px">Sign up for service <svg viewBox="0 0 7 10"><path d="M1 1l4 4-4 4" stroke="#fff" fill="none" stroke-width="1.5"/></svg></div>
  <div class="abs badge"><div class="badge-ring"></div>
    <div style="font-size:20px;line-height:22px">OVER</div>
    <div style="font-size:50px;line-height:52px;font-weight:500">45</div>
    <div style="font-size:20px;line-height:22px">YEARS</div>
  </div>
</section>

<section class="about">
  <div class="photo about-photo" role="img" aria-label="Woman taking white linens out of a washing machine into a laundry basket"></div>
  <div class="abs dots"></div>
  <div class="abs kicker" style="left:584px;top:136px">About</div>
  <h2 class="abs title" style="left:584px;top:163px">Corvell Laundry Company</h2>
  <p class="abs copy" style="left:584px;top:222px;width:450px">Corvell Laundry Company is a family-owned laundry service provider that has been serving Midtown Atlanta for over 45 years. We are proud to offer high quality and convenient services to the area residents and business owners and strive to keep our customers' clothing in tip top shape.</p>
  <div class="btn" style="left:584px;top:357px;width:124px;height:36px">Read more <svg viewBox="0 0 7 10"><path d="M1 1l4 4-4 4" stroke="#fff" fill="none" stroke-width="1.5"/></svg></div>
</section>

<section class="services">
  <h2 class="abs heading" style="left:171px;top:106px;font-size:44px;font-weight:300">Our <span style="color:var(--cyan);font-weight:500">Services</span></h2>
  <p class="abs copy" style="left:173px;top:186px;width:410px">Running a small business is not easy and the last thing you need is another tedious action item like doing laundry on your to-do list. Whether it is towels, linens or uniforms, outsourcing your launder needs to Corvell Laundry Company will allow you to focus on your business.</p>
  <div class="btn" style="left:173px;top:322px;width:124px;height:38px">Read more <svg viewBox="0 0 7 10"><path d="M1 1l4 4-4 4" stroke="#fff" fill="none" stroke-width="1.5"/></svg></div>
  <div class="abs svc-grid">
    <div class="svc"><span class="svc-icon" style="background:#d6dbe2" role="img" aria-label="Washing machine icon"></span>Commercial<br>Services</div>
    <div class="svc"><span class="svc-icon" style="background:#f2d51c" role="img" aria-label="Iron icon"></span>Light Commercial<br>Services</div>
    <div class="svc"><span class="svc-icon" style="background:#f6c24a" role="img" aria-label="Laundry basket icon"></span>Professional Laundry<br>Services</div>
    <div class="svc"><span class="svc-icon" style="background:#5a7bd8" role="img" aria-label="Delivery scooter icon"></span>Pickup and<br>Delivery</div>
    <div class="svc"><span class="svc-icon" style="background:#4a5cc4" role="img" aria-label="Folded clothes and iron icon"></span>Wash Dry<br>Fold</div>
    <div class="svc"><span class="svc-icon" style="background:#f07070" role="img" aria-label="Shirt on hanger icon"></span>Dry<br>Cleaning</div>
  </div>
</section>

<section class="why">
  <div class="photo why-photo" role="img" aria-label="Wicker basket of folded towels with white daisies"></div>
  <div class="abs kicker" style="left:614px;top:59px;letter-spacing:0;font-weight:300">Why choose</div>
  <h2 class="abs title" style="left:614px;top:84px">Corvell Laundry<br>Company</h2>
  <div class="abs" style="left:614px;top:186px;font-size:17px;color:var(--navy);font-weight:600">We Help You Optimize Your Time</div>
  <p class="abs copy" style="left:614px;top:216px;width:400px">Laundry is time consuming, especially for multi-tasking entrepreneurs. Corvell Laundry Company makes a simple promise, we will give you your time back to focus on your business</p>
  <div class="btn" style="left:613px;top:334px;width:125px;height:37px">Read more <svg viewBox="0 0 7 10"><path d="M1 1l4 4-4 4" stroke="#fff" fill="none" stroke-width="1.5"/></svg></div>
</section>

<section class="blog">
  <div class="abs heading" style="left:0;width:1200px;top:40px;text-align:center;color:var(--white);font-weight:300;font-size:19px">Blog</div>
  <h2 class="abs title" style="left:0;width:1200px;top:60px;text-align:center">Latest Blog</h2>
  <article class="card" style="left:173px"><div class="card-photo" role="img" aria-label="Blue basket full of colourful laundry"></div><div class="date"><div class="date-m">JUN</div><div class="date-d">18</div></div><div class="card-body"><div class="card-title">Proin commodo lacus ut venenatis</div><p class="card-text">Lorem ipsum dolor sit amet, coectetur adipiscing elit. Nam sit amet justo ac lorem tempus pretium sed eget nisi.</p><span class="card-link">READ MORE <svg width="6" height="9" viewBox="0 0 7 10"><path d="M1 1l4 4-4 4" stroke="#22b6e2" fill="none" stroke-width="1.5"/></svg></span></div></article>
  <article class="card" style="left:466px"><div class="card-photo" style="background:linear-gradient(135deg,#c8b7a4,#eef0ee)" role="img" aria-label="Mother and daughter in a laundromat"></div><div class="date"><div class="date-m">JUN</div><div class="date-d">20</div></div><div class="card-body"><div class="card-title">Proin commodo lacus ut venenatis</div><p class="card-text">Lorem ipsum dolor sit amet, coectetur adipiscing elit. Nam sit amet justo ac lorem tempus pretium sed eget nisi.</p><span class="card-link">READ MORE <svg width="6" height="9" viewBox="0 0 7 10"><path d="M1 1l4 4-4 4" stroke="#22b6e2" fill="none" stroke-width="1.5"/></svg></span></div></article>
  <article class="card" style="left:758px"><div class="card-photo" style="background:linear-gradient(135deg,#d8d6d2,#f4f4f2)" role="img" aria-label="Man loading a front-loading washing machine"></div><div class="date"><div class="date-m">JUN</div><div class="date-d">26</div></div><div class="card-body"><div class="card-title">Proin commodo lacus ut venenatis</div><p class="card-text">Lorem ipsum dolor sit amet, coectetur adipiscing elit. Nam sit amet justo ac lorem tempus pretium sed eget nisi.</p><span class="card-link">READ MORE <svg width="6" height="9" viewBox="0 0 7 10"><path d="M1 1l4 4-4 4" stroke="#22b6e2" fill="none" stroke-width="1.5"/></svg></span></div></article>
  <div class="arrow" style="left:153px;top:296px;background:var(--navy)"><svg width="10" height="16" viewBox="0 0 10 16"><path d="M8 1L2 8l6 7" stroke="#fff" fill="none" stroke-width="1.5"/></svg></div>
  <div class="arrow" style="left:1007px;top:296px;background:var(--cyan)"><svg width="10" height="16" viewBox="0 0 10 16"><path d="M2 1l6 7-6 7" stroke="#fff" fill="none" stroke-width="1.5"/></svg></div>
</section>

<section class="contact">
  <div class="abs contact-card">
    <div class="photo contact-photo" role="img" aria-label="Mother hugging her daughter beside a washing machine"></div>
    <div class="abs kicker" style="left:437px;top:32px;letter-spacing:0;font-weight:300">Contact us</div>
    <h2 class="abs title" style="left:437px;top:56px">Get in touch</h2>
    <div class="field" style="top:115px">Full Name</div>
    <div class="field" style="top:162px">Email Address</div>
    <div class="field" style="top:209px">Phone</div>
    <div class="field" style="top:256px;height:65px">Message</div>
    <div class="btn" style="left:440px;top:341px;width:125px;height:38px">Submit <svg viewBox="0 0 7 10"><path d="M1 1l4 4-4 4" stroke="#fff" fill="none" stroke-width="1.5"/></svg></div>
  </div>
</section>

<section class="newsletter">
  <div class="abs nl-title">NEWSLETTER <b>SIGNUP</b></div>
  <div class="abs nl-input">Enter Email Address <svg width="14" height="14" viewBox="0 0 24 24" fill="#22b6e2"><path d="M23 1L1 10l8 3 3 9z"/></svg></div>
</section>

<footer class="footer">
  <div class="brand" style="top:72px;left:173px"><span class="brand-dot"></span><span class="brand-name" style="color:#fff;font-size:18px;line-height:20px">Corvell<br>Laundry<br>Company</span></div>
  <div class="social"><span aria-label="Social link"></span><span aria-label="Social link"></span><span aria-label="Social link"></span></div>
  <div class="f-divider" style="left:343px"></div><div class="f-mark" style="left:341px"></div>
  <div class="f-divider" style="left:525px"></div><div class="f-mark" style="left:523px"></div>
  <div class="f-divider" style="left:773px"></div><div class="f-mark" style="left:771px"></div>
  <div class="f-col" style="left:391px"><h4>QUICK LINKS</h4><ul><li>Home</li><li>About Us</li><li>Why Choose Us</li><li>Services</li><li>Blog</li><li>Contact Us</li></ul></div>
  <div class="f-col" style="left:567px"><h4>SERVICES</h4><ul><li>Commercial Services</li><li>Light Commercial Services</li><li>Professional Laundry Services</li><li>Pickup and Delivery</li><li>Wash Dry Fold</li><li>Dry Cleaning</li></ul></div>
  <div class="f-col" style="left:815px;width:215px"><h4>CONTACT US</h4>
    <div class="contact-row"><svg width="9" height="12" viewBox="0 0 12 16" fill="#22b6e2"><path d="M6 0a6 6 0 0 1 6 6c0 4-6 10-6 10S0 10 0 6a6 6 0 0 1 6-6zm0 4a2 2 0 1 0 0 4 2 2 0 0 0 0-4z"/></svg><span>18 Linden Row, Midtown Atlanta</span></div>
    <div class="contact-row"><svg width="11" height="9" viewBox="0 0 24 18" fill="#22b6e2"><path d="M0 0h24v18H0z"/></svg><span>info@corvelllaundrycompany.com</span></div>
    <div class="contact-row"><svg width="11" height="11" viewBox="0 0 24 24" fill="#22b6e2"><path d="M6.6 10.8a15 15 0 0 0 6.6 6.6l2.2-2.2c.3-.3.7-.4 1-.2 1.1.4 2.3.6 3.6.6.6 0 1 .4 1 1V20c0 .6-.4 1-1 1A17 17 0 0 1 3 4c0-.6.4-1 1-1h3.5c.6 0 1 .4 1 1 0 1.3.2 2.5.6 3.6.1.3 0 .7-.2 1z"/></svg><span>01 234 567 890</span></div>
  </div>
  <div class="bottom-line"></div>
  <div class="copyright">Corvell Laundry Company</div>
  <div class="to-top"><svg width="30" height="14" viewBox="0 0 30 14"><path d="M1 13L15 1l14 12" stroke="#fff" fill="none" stroke-width="1.5"/></svg>GO TO TOP</div>
</footer>

</body>
</html>
```